依頼詳細
整骨院開業に合わせてポスティング用のチラシを配ろうと思います。そのチラシデザイン制作をお願い致します。三つ折りにして頭にくる部分にインパクトがあり、思わず中を開いて読んでくれるようなデザインをお願いします。ゴチャゴチャせず1つ1つがしっかり目に留まるようなものがよいです。できればデザインはほぼ一緒で構わないのですが、文句を少し変え開店後も配布できるデザインをもう1枚一緒に提案していただけると助かります。
記載項目
開院のお知らせ/
4月18日(木)
早川整骨院/
住所/
電話番号/
地図(参考図添付ファイル)駐車場院前あり/
院長似顔絵(参考図添付ファイル)/
ごあいさつ(参考添付ファイル)/
ロゴ(後程添付)/
診療時間    月~土曜 午前8:30~午後1:00
午後3:00~午後8:00
※土曜は午後6:00まで診療致します
日・祝祭日  休
急患時は問わず、随時診療致します。
交通事故・労災・各種保険取扱い/

診療内容(•骨折 •脱臼 •捻挫 •転倒 •スポーツでの痛み
•筋肉・関節の痛み(頚・肩・ひざ・ひじ・腰 ・手・足・など)•シビレ •肩こり
•リハビリ •テーピング •骨格調整
•その他・お体の不調の方はお気軽にご相談下さい。)
サイズ
A4
ページ数
片面
希望イメージ
シンプル 複雑
単色 カラフル
暗い 明るい
日常 高級
遊び心 厳粛
未来的 伝統的
女性的 男性的
希望する色
オレンジ、黄緑、白、明るめグレー、木目(看板は木目に白のカルプ文字使用)
納品ファイル
• 高解像度JPG (.jpg)
• イラストレーター形式 (.ai)
補足説明
・4月18日→よい骨(8)ゴロ合わせ的な(笑)
・地図作成お願いします。大き目で記載お願いします。
・似顔絵作成お願いします。
・診療時間は表でお願いします。
柔道整復師の広告の規制がありますので添付しときます。ただ皆さんいろんなことを広告記載しているようです。

印刷の関係などから良いのがあれば即決する場合もございます。ご了承ください
診療時間は表でお願いいたしますとしまさしたが、わかりやすければ何でもよいです。
住所、電話番号添付します。ロゴはもう少しお待ちください
遅くなり申し訳ございません。
ロゴを添付します。これってJPEGでいいですかね?
それともPDFが良いんですかね?
ロゴ、aiファイル添付致します。
よろしくお願いいたします。
皆さん、ご提案くださりありがとうございます。
後からいろいろ追加してすいません。
参考にロゴの別バージョンを添付しときます。
■ 選んだ理由

ご提案ありがとうございました。

見た目と色調がイメージとピッタリでした。
修正提案も迅速かつ丁寧にありがとうございました。

■ 提案者全員のお礼・コメント

たくさんのご提案ありがとうございました。

また機会がありましたら是非よろしくお願いします。

```html
<!DOCTYPE html>
<html lang="ja">
<head>
<meta charset="utf-8">
<title>早川整骨院 開院のお知らせ</title>
<link href="https://fonts.googleapis.com/css2?family=M+PLUS+Rounded+1c:wght@400;700;800;900&family=Noto+Sans+JP:wght@400;700;900&display=swap" rel="stylesheet">
<style>
:root{
  --orange:#f08a1c;
  --orange-deep:#e86f0c;
  --yellow:#fff3b8;
  --cream:#fffbe6;
  --green:#5cb82e;
  --green-deep:#2f9a34;
  --lime:#a6d64a;
  --gray:#d9d9d9;
  --gray-dark:#666;
  --ink:#333;
  --white:#fff;
}
*{margin:0;padding:0;box-sizing:border-box}
html,body{width:853px;height:1200px;overflow:hidden;background:var(--white)}
body{font-family:"Noto Sans JP",sans-serif;color:var(--ink)}
.flyer{position:relative;width:853px;height:1200px;
  background:repeating-linear-gradient(135deg,#ffe9a6 0 14px,#ffe08a 14px 28px);}
.header{position:absolute;left:40px;top:34px;width:773px;height:84px;background:var(--white);
  border-radius:42px;display:flex;align-items:center;justify-content:center;gap:18px;
  border:4px solid var(--orange)}
.brand-mark{width:50px;height:50px;background:var(--orange);border-radius:6px}
.brand-name{font-family:"M PLUS Rounded 1c",sans-serif;font-weight:900;font-size:52px;color:var(--green-deep);letter-spacing:4px}
.opening{position:absolute;left:40px;top:134px;width:773px;height:230px}
.date{position:absolute;left:20px;top:0;font-family:"M PLUS Rounded 1c",sans-serif;font-weight:900;
  font-size:170px;line-height:170px;color:var(--green-deep);letter-spacing:-4px}
.weekday{position:absolute;left:395px;top:40px;width:44px;height:110px;background:var(--white);border:3px solid var(--green-deep);
  writing-mode:vertical-rl;display:flex;align-items:center;justify-content:center;font-weight:900;font-size:22px;color:var(--green-deep)}
.pun{position:absolute;top:170px;display:flex;gap:0}
.pun span{display:inline-block;background:var(--orange);color:var(--white);font-family:"M PLUS Rounded 1c",sans-serif;
  font-weight:800;font-size:32px;padding:4px 18px;border-radius:10px}
.pun-1{left:28px}.pun-2{left:230px}
.kaiin{position:absolute;right:10px;top:20px;display:flex;gap:10px}
.kaiin span{width:150px;height:170px;background:var(--orange);border:5px solid var(--white);box-shadow:0 0 0 3px var(--orange);
  color:var(--white);font-family:"Noto Sans JP",sans-serif;font-weight:900;font-size:130px;line-height:160px;text-align:center}
.panel{position:absolute;left:40px;top:392px;width:773px;height:340px;background:var(--green);border-radius:10px;padding:12px}
.panel-inner{position:relative;width:100%;height:100%;background:var(--cream);border-radius:6px}
.portrait{position:absolute;left:14px;top:16px;width:240px;height:270px;border-radius:8px;
  background:radial-gradient(circle at 50% 40%,#fde3c5 0 40%,#f3c08a 70%,#e8a86a)}
.portrait-caption{position:absolute;left:20px;top:292px;font-size:14px;color:var(--ink)}
.greeting{position:absolute;left:272px;top:14px;width:470px}
.greeting h2{text-align:center;font-size:20px;color:var(--orange-deep);letter-spacing:6px;margin-bottom:6px}
.greeting p{font-size:12.5px;line-height:1.65}
.greeting .motto{font-size:19px;font-weight:900;color:var(--ink);margin:4px 0}
.services{position:absolute;left:272px;top:196px;width:470px;border:3px solid var(--orange);background:var(--yellow);border-radius:6px}
.services h3{background:var(--orange);color:var(--white);font-size:15px;padding:2px 10px;width:130px;border-radius:0 0 8px 0}
.services ul{list-style:none;padding:6px 12px;font-size:15px;font-weight:700;line-height:1.6}
.hours{position:absolute;left:48px;top:752px;width:540px;border-collapse:collapse;background:var(--white);font-size:17px}
.hours th,.hours td{border:2px solid var(--gray-dark);text-align:center;height:38px}
.hours th{background:var(--green);color:var(--white);font-weight:700}
.hours th.label{background:var(--orange)}
.hours td.time{font-weight:700;width:190px}
.hours .ok{color:var(--green-deep);font-weight:900}
.hours-note{position:absolute;left:48px;top:875px;font-size:13px;font-weight:700;line-height:1.5}
.access{position:absolute;left:604px;top:752px;width:209px;height:410px;background:var(--white);border:3px solid var(--green)}
.access h3{background:var(--green);color:var(--white);font-size:15px;text-align:center;padding:3px 0}
.map{position:absolute;left:6px;top:34px;right:6px;bottom:6px;background:linear-gradient(160deg,#eef3e6,#dfe6d3)}
.parking{position:absolute;right:10px;top:44px;background:var(--orange);color:var(--white);font-weight:900;font-size:15px;
  padding:6px 8px;writing-mode:horizontal-tb;border-radius:4px;line-height:1.3;text-align:center}
.footer{position:absolute;left:40px;top:930px;width:550px;height:232px;background:var(--white);border-radius:10px;padding:18px 22px}
.footer .brand{display:flex;align-items:center;gap:14px}
.footer .brand-mark{width:56px;height:56px;background:var(--green)}
.footer .brand-name{font-size:58px;color:var(--green-deep)}
.address{margin-top:14px;font-size:18px;font-weight:700}
.address span{margin-right:20px}
.phone{margin-top:8px;display:flex;align-items:center;gap:10px;font-family:"M PLUS Rounded 1c",sans-serif;
  font-weight:900;font-size:56px;color:var(--green-deep);letter-spacing:1px}
</style>
</head>
<body>
<div class="flyer">
  <div class="header">
    <div class="brand-mark"></div>
    <div class="brand-name">早川整骨院</div>
  </div>

  <section class="opening">
    <div class="date">4.18</div>
    <div class="weekday">木曜日</div>
    <div class="pun pun-1"><span>よい</span></div>
    <div class="pun pun-2"><span>ほね</span></div>
    <div class="kaiin"><span>開</span><span>院</span></div>
  </section>

  <section class="panel">
    <div class="panel-inner">
      <div class="portrait" role="img" aria-label="院長の似顔絵イラスト"></div>
      <div class="portrait-caption">院長　早川</div>
      <div class="greeting">
        <h2>ごあいさつ</h2>
        <p>このたび、佐野市で整骨院を開院する運びとなりました。地域の皆さまが健康で快適な毎日を過ごせるよう、一人ひとりのお体に丁寧に向き合い、心を込めて施術いたします。お気軽にご来院ください。</p>
        <p class="motto">「いつも明るく、元気で、前向きに」</p>
        <p>を合言葉に、スタッフ一同皆さまのご来院を心よりお待ちしております。</p>
      </div>
      <div class="services">
        <h3>診療内容</h3>
        <ul>
          <li>※骨折※脱臼※捻挫※転倒※スポーツでの痛み</li>
          <li>※筋肉・関節の痛み（頚・肩・ひざ・ひじ・腰・手・足）</li>
          <li>※シビレ※肩こり※リハビリ※テーピング※骨格調整</li>
        </ul>
      </div>
    </div>
  </section>

  <table class="hours">
    <tr><th class="label">診療時間</th><th>月</th><th>火</th><th>水</th><th>木</th><th>金</th><th>土</th><th>日</th></tr>
    <tr><td class="time">午前8:30〜午後1:00</td><td class="ok">●</td><td class="ok">●</td><td class="ok">●</td><td class="ok">●</td><td class="ok">●</td><td class="ok">●</td><td>休</td></tr>
    <tr><td class="time">午後3:00〜午後8:00</td><td class="ok">●</td><td class="ok">●</td><td class="ok">●</td><td class="ok">●</td><td class="ok">●</td><td class="ok">▲</td><td>休</td></tr>
  </table>
  <p class="hours-note">▲土曜は午後6:00まで　日・祝祭日休　急患時は随時診療致します<br>交通事故・労災・各種保険取扱い</p>

  <section class="access">
    <h3>アクセスマップ</h3>
    <div class="map" role="img" aria-label="整骨院周辺の地図"></div>
    <div class="parking">駐車場<br>院前あり</div>
  </section>

  <footer class="footer">
    <div class="brand">
      <div class="brand-mark"></div>
      <div class="brand-name">早川整骨院</div>
    </div>
    <p class="address"><span>〒327-0000</span>栃木県佐野市みどり町1234-5</p>
    <p class="phone">
      <svg width="50" height="50" viewBox="0 0 24 24" aria-hidden="true"><circle cx="12" cy="12" r="12" fill="#2f9a34"/><path fill="#fff" d="M8.6 5.5l1.9 3.2-1.3 1.3c.8 1.7 2.1 3 3.8 3.8l1.3-1.3 3.2 1.9-.8 2.6c-5.2-.3-9.7-4.8-10-10z"/></svg>
      0283-00-1234
    </p>
  </footer>
</div>
</body>
</html>
```